Wordpress Design for a Digital Management Consulting Business

I need a simple Wordpress Design and someone to set it up for a new boutique management consulting business called Tidewell Advisory that specialises in providing strategic advice to help grow digital businesses. It covers business strategy, marketing strategy, digital strategy, web product development, marketing campaigns, social, search, etc. From strategy to implementation.

URL is: tidewelladvisory.com.au

My professional background is here: au.examplenet.com/in/norabellweather

Competitors: other boutique digital/marketing management consulting businesses in Australia

The logos, colours and fonts are attached.

I would like the site to convey a business that is Smart/intelligent, Contemporary, Progressive, Digital, Energetic, Friendly.

The objective of the site is to educate visitors about what Tidewell Advisory does and encourage them to contact me for more information. It will be very light on content.

Target Market(s)

CEOs/Managing Directors, General Managers, Marketing Directors

Industry/Entity Type

Management Consulting

Font styles to use
Sans Serif

Colors
e34197
5c5c5c
000000

Requirements
Must have
• Site design requirements:
• Choose an appropriate Wordpress template, set it up for me and let me be able to edit it ongoing.
• It should use lots of images - these can be inspirational and not necessarily tied directly to the work
• Pink should feature, but not be the dominant colour.
• Site structure should be:
• 1. Home page - image led with horizontal navigation. Text beneath and images to describe the services.
• 2. About page - with space to write text and insert a picture of the Director
• 3. Services - with space to highlight services either as a list or graphically with text
• 4. Contact page - with space to write text and add email links, etc.
• Should have horizontal navigation
• It should have the flexibility to add another page
Nice to have
• Use the tree icon somehow in the design - consider in the background enlarged
• Use pink, grey, black from logo. Can introduce another complimentary colour if necessary.
• Can introduce another complimentary font to go with the logo font.
Should not have
• Use cliched business images and icons, eg. business suits, hand shakes, business men, business ties.

```html
<!DOCTYPE html>
<html lang="en">
<head>
<meta charset="utf-8">
<title>Tidewell Advisory</title>
<link href="https://fonts.googleapis.com/css2?family=Open+Sans:wght@400;600;700&display=swap" rel="stylesheet">
<style>
:root{
  --pink:#e34197;
  --pink-soft:#e86aa8;
  --grey:#5c5c5c;
  --black:#000000;
  --bg-light:#ececec;
  --bg-mid:#bdbdbd;
  --panel-top:#a7a7a7;
  --panel-bottom:#b9b9b9;
  --white:#ffffff;
}
*{box-sizing:border-box;margin:0;padding:0}
html,body{width:809px;height:1200px;overflow:hidden}
body{font-family:"Open Sans",Arial,sans-serif;color:var(--black);
  background:radial-gradient(ellipse at 50% 30%,#f6f6f6 0%,var(--bg-light) 35%,var(--bg-mid) 100%);position:relative}
.site-header{position:absolute;left:0;top:0;width:809px;height:110px}
.brand{position:absolute;left:20px;top:24px;display:flex;align-items:center;gap:10px}
.brand-mark{width:34px;height:34px;border-radius:50%;background:var(--pink)}
.brand-name{font-size:26px;font-weight:600;color:var(--pink);letter-spacing:2px;line-height:1}
.brand-sub{font-size:11px;letter-spacing:5px;color:var(--grey);margin-top:4px}
.search{position:absolute;right:10px;top:40px;width:84px;height:16px;border:1px solid #bbb;border-radius:8px;background:var(--white)}
.search svg{position:absolute;left:4px;top:2px}
.main-nav{position:absolute;left:390px;top:82px;display:flex;gap:14px;font-size:12px}
.main-nav a{display:flex;align-items:center;gap:4px;color:var(--black);text-decoration:none}
.main-nav .dot{width:16px;height:16px;border-radius:50%;background:#222}
.main-nav a.active{background:#222;color:var(--white);padding:1px 8px 1px 3px;border-radius:4px}
.main-nav a.active .dot{background:var(--pink)}
.hero{position:absolute;left:180px;top:122px;width:450px;height:272px;border-radius:10px;border:6px solid #f6f6f6;
  background:linear-gradient(180deg,#6a6a6a,#4a4a4a);box-shadow:0 4px 12px rgba(0,0,0,.35);display:flex;align-items:center;justify-content:center;color:#eee;font-size:15px}
.hero-controls{position:absolute;left:340px;top:392px}
.intro{position:absolute;left:10px;top:430px;width:789px;text-align:center;font-size:12.5px;font-weight:600;line-height:16px}
.panel{position:absolute;left:10px;width:789px;border-radius:10px;border:1px solid rgba(255,255,255,.55);
  background:linear-gradient(180deg,var(--panel-top),var(--panel-bottom))}
.panel-title{position:absolute;left:12px;top:6px;color:var(--white);font-size:14px;font-weight:600;letter-spacing:1px}
.services{top:528px;height:255px}
.approach{top:800px;height:266px}
.cards{position:absolute;left:0;top:44px;width:100%;display:flex;justify-content:space-around}
.card{width:200px;text-align:center}
.card-visual{width:86px;height:86px;border-radius:50%;margin:0 auto 14px}
.v1{background:radial-gradient(circle,#2a5d9c,#0c2447)}
.v2{background:conic-gradient(#e33 0 20%,#f90 0 40%,#3a3 0 60%,#29c 0 80%,#94c 0)}
.v3{background:conic-gradient(#c22 0 25%,#f80 0 50%,#4a3 0 75%,#36b 0)}
.v4{background:conic-gradient(#27c 0 33%,#f80 0 66%,#c33 0)}
.v5{background:radial-gradient(circle,#fff 30%,#39c 32%,#e84 70%)}
.v6{background:conic-gradient(#7c3 0 33%,#c3c 0 66%,#38c 0)}
.card-title{font-size:10px;font-weight:700;color:#222;margin-bottom:4px;letter-spacing:.5px}
.card-text{font-size:9.5px;color:var(--white);line-height:12px;text-shadow:0 1px 1px rgba(0,0,0,.35)}
.site-footer{position:absolute;left:0;top:1090px;width:809px;height:110px;background:var(--pink-soft);text-align:center}
.footer-nav{margin-top:22px;display:flex;justify-content:center;gap:10px;font-size:15px}
.footer-nav a{color:var(--white);text-decoration:none}
.copyright{color:var(--white);font-size:8px;margin-top:4px}
</style>
</head>
<body>
<header class="site-header">
  <div class="brand">
    <span class="brand-mark"></span>
    <div><div class="brand-name">TIDEWELL</div><div class="brand-sub">ADVISORY</div></div>
  </div>
  <div class="search"><svg width="10" height="10" viewBox="0 0 10 10"><circle cx="4" cy="4" r="3" fill="none" stroke="#888"/><line x1="6" y1="6" x2="9" y2="9" stroke="#888"/></svg></div>
  <nav class="main-nav">
    <a class="active" href="#"><span class="dot"></span>Home</a>
    <a href="#"><span class="dot"></span>About</a>
    <a href="#"><span class="dot"></span>Services</a>
    <a href="#"><span class="dot"></span>Clients</a>
    <a href="#"><span class="dot"></span>Contact</a>
  </nav>
</header>

<section class="hero" role="img" aria-label="Rotating feature image with headline">Text/Image/Typography</section>
<svg class="hero-controls" width="130" height="32" viewBox="0 0 130 32">
  <polygon points="2,16 30,4 30,28" fill="#3a9a3a"/>
  <polygon points="128,16 100,4 100,28" fill="#3a9a3a"/>
  <ellipse cx="65" cy="16" rx="28" ry="11" fill="#fff" stroke="#ccc"/>
</svg>

<p class="intro">Tidewell Advisory is a boutique management consulting company advising digital businesses across business<br>product and marketing strategy. Combining strategic thinking with digital knowhow and marketing expertise<br>Tidewell Advisory works with businesses looking to develop their digital capabilities or<br>wanting to accelerate the growth of a new or existing digital business</p>

<section class="panel services">
  <h2 class="panel-title">SERVICES</h2>
  <div class="cards">
    <div class="card"><div class="card-visual v1" role="img" aria-label="Digital strategy diagram"></div><p class="card-text">Clear digital strategy shaped<br>around your goals, your market<br>and the growth you want to reach<br>over the coming years</p></div>
    <div class="card"><div class="card-visual v2" role="img" aria-label="Marketing strategy cycle diagram"></div><p class="card-text">Marketing plans that connect<br>brand, campaigns, social and<br>search into one steady program<br>with results you can measure</p></div>
    <div class="card"><div class="card-visual v3" role="img" aria-label="Product development diagram"></div><p class="card-text">Web product development from<br>early concept through launch,<br>guided by real customer needs<br>and sound business sense</p></div>
  </div>
</section>

<section class="panel approach">
  <h2 class="panel-title">WHAT WE DO?</h2>
  <div class="cards">
    <div class="card"><div class="card-visual v4" role="img" aria-label="Strategic thinking illustration"></div><h3 class="card-title">STRATEGIC THINKING</h3><p class="card-text">Big picture advice grounded<br>in practical steps you can<br>start acting on right away</p></div>
    <div class="card"><div class="card-visual v5" role="img" aria-label="Analytical approach illustration"></div><h3 class="card-title">ANALYTICAL APPROACH</h3><p class="card-text">Decisions built on data,<br>testing and honest review<br>of what truly works well</p></div>
    <div class="card"><div class="card-visual v6" role="img" aria-label="Project management illustration"></div><h3 class="card-title">PROJECT MANAGEMENT</h3><p class="card-text">Hands on delivery that takes<br>strategy all the way through<br>to a working implementation</p></div>
  </div>
</section>

<footer class="site-footer">
  <nav class="footer-nav"><a href="#">Home</a><a href="#">About</a><a href="#">Services</a><a href="#">Clients</a><a href="#">Contact</a></nav>
  <p class="copyright">Copyright©2011</p>
</footer>
</body>
</html>
```